I need a new business card for my hair salon based in Fairfax, VA called "Lune's Salon". I have been in business at the same location for the past 15 years, and have recently remodeled the place to be a little bit more upscale and modern. Previously, my clientele's were mostly men, but now I would like to attract more female clientele into my business. I would like the design to attract the female's attention with it's modern touch, flowery, freshness with just enough information and not too compact. Simple, clean and professional is the look.
Requirements
Must Have:
- The design should include:
Business name: Lune's Salon
Hairstylist/Owner Name: Lune Okafor
Phone Number: (555) 418-6037
Website: www.lunehairstudio.example
Address: 48390 Harlow Penn Circle
Fairfax, VA 20517
FRONT CARD should include:
- Logo (Business name)
- Slogan (Soft curls, bright days)
BACK CARD should include:
- Logo (Business name)
- Hairstyle name
- Phone number
- Website
- Address
Reason: There were some good submission for this project, but most of the submission were poorly designed, and did not have what I want. There isn't enough designs for me to choose from and not one of it stood out to me. I would like to extend it a bit longer to see if any other designer would step up to the plate, and deliver. Thank you.
Requirements
Must have
- The front side of the business card should only have the business name (Lune's Salon) and slogan, (Soft curls bright days) with a creative design.
The back side of the business card should have all the business information, and creative design that matches with the front, but not identical.
The first letter (V) in (Lune's) should have a flower design connected to it, which blends into the background design.
Nice to have
- Light color scheme.
Should not have
- The front, and back should not have the same design.
Do not include illustrations of a pair of scissors, combs or any objects in the design.
The design should not take the main focus from the business name and business information. It should blend well together... if that's possible.

```html
<!DOCTYPE html>
<html lang="en">
<head>
<meta charset="utf-8">
<title>Lune's Salon – Business Card Front</title>
<link rel="stylesheet" href="https://fonts.googleapis.com/css2?family=Lobster&display=swap">
<style>
  :root {
    --card-violet: #7a5aff;
    --ink-white: #ffffff;
  }
  html, body {
    margin: 0;
    padding: 0;
    width: 1200px;
    height: 702px;
    overflow: hidden;
    background: var(--card-violet);
  }
  .card-front {
    position: relative;
    width: 1200px;
    height: 702px;
    background: var(--card-violet);
    color: var(--ink-white);
    font-family: "Lobster", cursive;
  }
  .brand-lockup {
    position: absolute;
    left: 0;
    right: 0;
    top: 236px;
    text-align: center;
  }
  .business-name {
    margin: 0;
    font-size: 150px;
    font-weight: 400;
    line-height: 1;
    letter-spacing: 6px;
    white-space: nowrap;
  }
  .slogan {
    margin: 4px 0 0;
    font-size: 38px;
    font-weight: 400;
    line-height: 1;
    letter-spacing: 5px;
    text-transform: uppercase;
    white-space: nowrap;
  }
</style>
</head>
<body>
  <main class="card-front">
    <div class="brand-lockup">
      <h1 class="business-name">Lune's Salon</h1>
      <p class="slogan">Soft curls, bright days</p>
    </div>
  </main>
</body>
</html>
```